Building company with a modern and unique product looking for a business card to help us stand out

We currently have a logo but as our business has grown, we feel that our business card is not reflecting our modern and high quality product and help us stand out from the crowd. Our business is mainly in the construction of new homes using a unique method and materials that makes our homes fire proof, vermin and pest resistant and rated to the maximum cyclone category (category 5). We need a business card that helps us stand out as well as communicating professionalism, high quality and trustworthiness. I have attached our current logo with a black and white option, as well as our business card which is double sided. We would like to retain as much of the information that is currently on our business cards, but presented in a more sleek way. We do like our current colour palette ( white, black, yellow and grey) and have been looking primarily at business cards with a black background however we are open to other combinations of colour and layout as long as we stand out. Please feel free to tweak our logo to make it more suitable for a business card, we like the black option that we use but we have had trouble trying to get the white area to match the rest of the logo and blend effectively into a business card. Please do not hesitate to contact us with any questions as we really want this to be successful!

Target Market(s)

Large contracts including government and larger companies

Industry/Entity Type

Business

Contact Information for Business Card

We will be providing this business card to potential clients including key government ministers and large funding companies, our business card should show that we are professional and reliable.

Requirements
Must have
• It must be easy to read and pleasing to the eye, It must contain as much of the information on the current business card and unless something really stands out, we will most likely pick a design that has all of the information included. It must include our logo of course and have some colour included.
Nice to have
• We are looking for a high end business card and would like to see designs that reflect this. We like the gloss/matte contrast, plastic cards with opaque/coloured areas and unique features not seen on everyday paper business cards. It would be nice to see a few different colour combinations, we are open to new ideas so please feel free to take some artistic licence.
Should not have
• Must not be too busy, difficult to read or be distracting from the information conveyed. Other than this please feel free to add your own touches and make it unique!

```html
<!DOCTYPE html>
<html lang="en">
<head>
<meta charset="utf-8">
<title>Kestrel Building Company – Business Card</title>
<link rel="stylesheet" href="https://fonts.googleapis.com/css2?family=Libre+Baskerville:wght@400;700&family=Open+Sans:wght@400&display=swap">
<style>
  :root {
    --stage: #3b3b3b;
    --paper: #f0f0f0;
    --ink: #111111;
    --ink-soft: #444444;
    --gold: #b8962a;
    --night: #000000;
    --snow: #ffffff;
  }
  * { margin: 0; padding: 0; box-sizing: border-box; }
  html, body {
    width: 1200px;
    height: 750px;
    overflow: hidden;
    background: var(--stage);
  }
  .stage {
    position: relative;
    width: 1200px;
    height: 750px;
  }
  .card {
    position: absolute;
    top: 228px;
    width: 461px;
    height: 263px;
  }
  .card--front { left: 124px; background: var(--paper); }
  .card--back  { left: 618px; background: var(--night); }

  .person {
    position: absolute;
    left: 38px;
    top: 81px;
  }
  .person__name {
    font-family: "Libre Baskerville", serif;
    font-weight: 700;
    font-size: 17px;
    letter-spacing: 0.5px;
    color: var(--ink);
  }
  .person__role {
    font-family: "Libre Baskerville", serif;
    font-weight: 400;
    font-size: 12px;
    color: var(--gold);
    margin-top: 2px;
  }
  .contacts {
    position: absolute;
    left: 38px;
    top: 132px;
    list-style: none;
  }
  .contacts li {
    display: flex;
    align-items: center;
    height: 17.6px;
    font-family: "Open Sans", sans-serif;
    font-size: 11px;
    color: var(--ink-soft);
  }
  .contacts svg {
    width: 12px;
    height: 12px;
    margin-right: 6px;
    fill: var(--ink);
  }

  .brand {
    position: absolute;
    right: 38px;
    top: 98px;
    display: flex;
    align-items: center;
    gap: 10px;
  }
  .brand__mark {
    width: 14px;
    height: 14px;
    background: var(--gold);
  }
  .brand__name {
    font-family: "Libre Baskerville", serif;
    font-weight: 400;
    font-size: 20px;
    line-height: 1.25;
    color: var(--ink);
  }
  .brand__name span { display: block; }

  .back-brand {
    position: absolute;
    left: 0;
    right: 0;
    top: 112px;
    text-align: center;
    font-family: "Libre Baskerville", serif;
    font-weight: 400;
    font-size: 26px;
    color: var(--snow);
  }
  .back-web {
    position: absolute;
    left: 0;
    right: 0;
    top: 208px;
    text-align: center;
    font-family: "Open Sans", sans-serif;
    font-size: 11px;
    letter-spacing: 7px;
    color: var(--snow);
  }
</style>
</head>
<body>
<main class="stage">
  <section class="card card--front">
    <div class="person">
      <h1 class="person__name">Orwell Pike</h1>
      <p class="person__role">Managing Director</p>
    </div>
    <ul class="contacts">
      <li>
        <svg viewBox="0 0 24 24" aria-hidden="true"><path d="M6.6 10.8a15.1 15.1 0 0 0 6.6 6.6l2.2-2.2a1 1 0 0 1 1-.25 11.4 11.4 0 0 0 3.6.57 1 1 0 0 1 1 1V20a1 1 0 0 1-1 1A17 17 0 0 1 3 4a1 1 0 0 1 1-1h3.5a1 1 0 0 1 1 1c0 1.25.2 2.45.57 3.57a1 1 0 0 1-.25 1z"/></svg>
        0400 555 317
      </li>
      <li>
        <svg viewBox="0 0 24 24" aria-hidden="true"><path d="M7 1h10a2 2 0 0 1 2 2v18a2 2 0 0 1-2 2H7a2 2 0 0 1-2-2V3a2 2 0 0 1 2-2zm0 3v14h10V4z"/></svg>
        (02) 55 510 384
      </li>
      <li>
        <svg viewBox="0 0 24 24" aria-hidden="true"><path d="M2 5h20v14H2z M3.5 6.5 12 13l8.5-6.5" stroke="#f0f0f0" stroke-width="1.5"/></svg>
        kestrelbuild@harbourmail.com
      </li>
      <li>
        <svg viewBox="0 0 24 24" aria-hidden="true"><circle cx="12" cy="12" r="10"/><path d="M2 12h20M12 2c3 3 3 17 0 20M12 2c-3 3-3 17 0 20" stroke="#f0f0f0" stroke-width="1.3" fill="none"/></svg>
        www.harbourmail.com
      </li>
    </ul>
    <div class="brand">
      <span class="brand__mark" aria-hidden="true"></span>
      <p class="brand__name"><span>Kestrel</span><span>Building Company</span></p>
    </div>
  </section>

  <section class="card card--back">
    <p class="back-brand">Kestrel Building Company</p>
    <p class="back-web">www.harbourmail.com</p>
  </section>
</main>
</body>
</html>
```